Nutrivana, site for appointments between nutritionists and patients

Nutrivana is a platform for connecting nutritionists and patients with appointment scheduling and online payment.

We like teal, but we're not fixated on it.

The site must be simple, accessible and pleasant and dynamic and evoke the joy of nutrition while not forgetting the health aspect.

Example of illustration which tend towards what we are looking for.

Logo and graphic charter

Home page, simple little information

1)
Book a physical or video consultation with a dietitian (medirendo, you stay calm, lorée, vantoc)

2)
Reason for using Nutrivana

Access state-certified nutrition experts with several years of training (registration of professionals on the site only with adeli number and valid diploma)

Access the availability of tens of thousands of healthcare professionals.

Make an appointment online, 24/7, for a physical or video consultation.

Secure personal data

3)
You are a dietitian nutritionist

Use nutrivana to optimize your activity
Free up time by making an appointment online
Limit unfulfilled appointments with online payment
Take advantage of Nutrivana's notoriety to obtain better visibility
Use a commercial platform to develop your patient base
Use the platform's communication tools
Etc ...

Page 2 if applicable

List of professionals

Page 3 if search by specific name

Name photo
The essentials, map and access information, presentation, timetables, prices, site, make an appointment

Page 3 bis more in-depth presentation.

Page 4
agenda appointment booking page

Payment page

Professional page

Page 1
presentation of assets

Page 2 limited access

Rates with bronze, silver, gold, platinum account

Products, training and services page for sale

Blog page

Nutrivana is a platform that connects nutritionists and patients with online appointments and payment.

We like the teal color but we are not set on it.

The site must be simple, accessible, pleasant and dynamic and evoke the joy of nutrition while not forgetting the health aspect.

Example of illustrations that tend towards what we are looking for.

Our Logo is on the attachment

Home page

1)
Book a physical or video consultation with a dietician (ex site: medirendo, you stay calm, lorée, vantoc)

2)
Reasons to use Nutrivana

Access to experts in nutrition with several years of training (registration of professionals on the site only with adeli number and valid diploma)

Access the availability of tens of thousands of dieticians.

Secure personal data

3) You are a dietitian nutritionist

Free up time with online appointment booking
Limit the number of missed appointments thanks to online payment
Take advantage of Nutrivana's notoriety to get a better visibility
Use the communication tools of the platform
Etc ...

Page 2 if the patient don't choose a professional and put only a place.

List of professionals

Page 3 if searching by specific name

Photo name
The essentials, map and access information, presentation, opening hours, rates, site, make an appointment

Page 3 bis - more detailed presentation of dietician.

Page 4
diary page for making an appointment

Payment page

Blog page

Side Professional page

Page 1
presentation of assets

Page 2 (limited access)

Page 3

Products, training and services for sale page

Pour laisser le temps aux designers de travailler.

Target Market(s)

The general public

Number of Pages Required

5+ page

Colors
00AB8E
00BBA5
67D7C9
C6EFE9
E9F9F6

Requirements
Must have
• Read the project in the attached documents. Read the project on the attachments
Should not have
• No photographs

```html
<!DOCTYPE html>
<html lang="en">
<head>
<meta charset="utf-8">
<title>Nutrivana</title>
<link href="https://fonts.googleapis.com/css2?family=Poppins:wght@400;500;600&display=swap" rel="stylesheet">
<style>
:root{
  --bg:#eef8f7;
  --green-dark:#0a8b54;
  --green:#149459;
  --green-mid:#22a56c;
  --teal:#3fbfb2;
  --teal-light:#67d7c9;
  --mint:#c6efe9;
  --nav:#2cb58c;
  --white:#ffffff;
  --grey:#8a8f8e;
  --ink:#1f3b33;
}
*{margin:0;padding:0;box-sizing:border-box}
html,body{width:1200px;height:3679px;overflow:hidden}
body{position:relative;background:var(--bg);font-family:'Poppins',sans-serif;color:var(--ink)}
.abs{position:absolute}
.bg-waves{position:absolute;left:0;top:0;width:1200px;height:3679px}
.brand{display:flex;align-items:center;gap:10px;font-family:'Poppins',sans-serif;font-weight:600}
.brand-dot{border-radius:50%;background:var(--green-mid)}
.site-brand{left:150px;top:116px;font-size:28px;color:var(--green);white-space:nowrap}
.site-brand .brand-dot{width:20px;height:20px}
.nav{left:351px;top:124px;font-size:19px;color:var(--nav)}
.nav a{position:absolute;white-space:nowrap;text-decoration:none;color:var(--nav)}
.btn{display:flex;align-items:center;justify-content:center;border-radius:34px;text-decoration:none;font-weight:500}
.btn-primary{background:linear-gradient(90deg,#17a067,#3fbfa8);color:var(--white);font-size:18px;box-shadow:0 4px 8px rgba(0,90,60,.25)}
.header-book{left:889px;top:39px;width:161px;height:47px}
.hero-book{left:164px;top:517px;width:162px;height:47px}
.hero-title{left:164px;top:338px;font-size:48px;font-weight:500;color:var(--green)}
.hero-name{left:160px;top:398px;font-size:82px;font-weight:600;color:var(--green-mid);letter-spacing:-1px}
.art{border-radius:46% 54% 50% 50% / 52% 46% 54% 48%}
.hero-art{left:620px;top:257px;width:530px;height:536px;background:radial-gradient(circle at 45% 45%,#17a066,#9fdcc3)}
.consult-art{left:69px;top:1071px;width:488px;height:393px;background:radial-gradient(circle at 50% 50%,#e9f5ef,#3cb886)}
.reason-art{left:586px;top:1729px;width:585px;height:457px;background:radial-gradient(circle at 55% 50%,#8fd9cf,#3fbfb2)}
.h2{font-size:38px;font-weight:500;color:var(--white);line-height:42px}
.consult-title{left:613px;top:1085px}
.partner{background:var(--white);color:var(--ink);font-size:21px;width:206px;height:67px;position:absolute;box-shadow:0 4px 10px rgba(0,60,40,.15)}
.reason-title{left:149px;top:1762px}
.reasons{left:149px;top:1882px;width:440px;list-style:none}
.reasons li{position:absolute;left:0;width:440px;display:flex;gap:18px;font-size:17.5px;line-height:21px;color:var(--white)}
.tick{flex:none;width:46px;height:46px;border-radius:50%;background:var(--white);display:flex;align-items:center;justify-content:center;box-shadow:0 2px 6px rgba(0,60,50,.2)}
.reasons p{padding-top:2px}
.pro-title{left:0;top:2318px;width:1200px;text-align:center;font-size:40px;font-weight:500;color:var(--white)}
.card{position:absolute;width:250px;height:264px;background:var(--white);border-radius:70px 30px 70px 30px;box-shadow:0 6px 16px rgba(0,80,70,.12);display:flex;flex-direction:column;align-items:center;padding-top:26px;text-align:center}
.card svg{height:96px}
.card p{margin-top:18px;font-size:18px;line-height:21.5px;color:var(--grey);width:200px}
.footer-links{left:283px;top:3403px;list-style:none}
.footer-links li{font-size:19px;line-height:29.3px;color:var(--white)}
.footer-brand{left:0;width:1200px;top:3400px;flex-direction:column;font-size:52px;color:var(--white);gap:14px}
.footer-brand .brand-dot{width:110px;height:110px;background:var(--white)}
.contact{left:797px;top:0;list-style:none}
.contact li{position:absolute;left:0;display:flex;align-items:center;gap:22px;color:var(--white);font-size:19px;line-height:27px;white-space:nowrap}
.contact .ico{width:52px;height:52px;border-radius:50%;border:2px solid rgba(255,255,255,.8);display:flex;align-items:center;justify-content:center}
.copyright{left:0;top:3638px;width:1200px;text-align:center;font-size:16px;color:var(--white)}
</style>
</head>
<body>
<svg class="bg-waves" viewBox="0 0 1200 3679" aria-hidden="true">
  <defs>
    <linearGradient id="bandGrad" gradientUnits="userSpaceOnUse" x1="0" y1="760" x2="0" y2="2530">
      <stop offset="0" stop-color="#0a8b54"/>
      <stop offset=".35" stop-color="#1fa06a"/>
      <stop offset=".6" stop-color="#35b98f"/>
      <stop offset="1" stop-color="#44c2b6"/>
    </linearGradient>
    <linearGradient id="footGrad" gradientUnits="userSpaceOnUse" x1="0" y1="3110" x2="0" y2="3679">
      <stop offset="0" stop-color="#0d8e56"/>
      <stop offset="1" stop-color="#2fb27a"/>
    </linearGradient>
  </defs>
  <path fill="url(#bandGrad)" d="M0 874 C120 760 260 720 380 790 C470 845 520 900 620 880 C760 850 900 800 1000 930 C1080 1030 1130 1086 1200 1086 V2443 C1040 2450 860 2580 640 2560 C420 2540 220 2470 0 2529 Z"/>
  <path fill="#c6efe9" opacity=".7" d="M380 3160 C560 3120 760 3240 900 3275 C1040 3310 1140 3330 1200 3335 V3380 C1140 3370 1040 3340 900 3320 C760 3300 620 3220 440 3150 Z"/>
  <path fill="url(#footGrad)" d="M0 3243 C140 3130 290 3090 440 3150 C620 3220 760 3300 900 3320 C1040 3340 1140 3370 1200 3380 V3679 H0 Z"/>
</svg>

<header>
  <div class="abs brand site-brand"><span class="brand-dot"></span>nutrivana</div>
  <nav class="abs nav">
    <a style="left:0">Home</a>
    <a style="left:96px">Professionals</a>
    <a style="left:260px">Search</a>
    <a style="left:370px">Appointment</a>
    <a style="left:533px">Payment</a>
    <a style="left:658px">Blog</a>
  </nav>
  <a class="abs btn btn-primary header-book">Book Now</a>
</header>

<section class="hero">
  <h1 class="abs hero-title">Welcome to</h1>
  <div class="abs hero-name">nutrivana</div>
  <a class="abs btn btn-primary hero-book">Book Now</a>
  <div class="abs art hero-art" role="img" aria-label="Illustration of a woman leaning on a large phone showing the app with a green smoothie"></div>
</section>

<section class="consult">
  <div class="abs art consult-art" role="img" aria-label="Illustration of a diet plan on a phone with vegetables and a person using a laptop"></div>
  <h2 class="abs h2 consult-title">Book a physical<br>or video consultation<br>with a dietitian</h2>
  <a class="btn partner" style="left:613px;top:1245px">medirendo</a>
  <a class="btn partner" style="left:837px;top:1245px">you stay calm</a>
  <a class="btn partner" style="left:613px;top:1336px">lorée</a>
  <a class="btn partner" style="left:837px;top:1336px">vantoc</a>
</section>

<section class="reasons-block">
  <h2 class="abs h2 reason-title">Reason for<br>using Nutrivana</h2>
  <ul class="abs reasons">
    <li style="top:0"><span class="tick"><svg width="24" height="24" viewBox="0 0 24 24"><path d="M4 12.5l5 5L20 6" fill="none" stroke="#1fa06a" stroke-width="4" stroke-linecap="round" stroke-linejoin="round"/></svg></span><p>Access state-certified nutrition experts with several years of training (registration of professionals on the site only with adeli number and valid diploma)</p></li>
    <li style="top:104px"><span class="tick"><svg width="24" height="24" viewBox="0 0 24 24"><path d="M4 12.5l5 5L20 6" fill="none" stroke="#1fa06a" stroke-width="4" stroke-linecap="round" stroke-linejoin="round"/></svg></span><p>Access the availability of tens of thousands of healthcare professionals.</p></li>
    <li style="top:187px"><span class="tick"><svg width="24" height="24" viewBox="0 0 24 24"><path d="M4 12.5l5 5L20 6" fill="none" stroke="#1fa06a" stroke-width="4" stroke-linecap="round" stroke-linejoin="round"/></svg></span><p>Make an appointment online, 24/7, for a physical or video consultation.</p></li>
    <li style="top:266px"><span class="tick"><svg width="24" height="24" viewBox="0 0 24 24"><path d="M4 12.5l5 5L20 6" fill="none" stroke="#1fa06a" stroke-width="4" stroke-linecap="round" stroke-linejoin="round"/></svg></span><p style="padding-top:11px">Secure personal data</p></li>
  </ul>
  <div class="abs art reason-art" role="img" aria-label="Illustration of two patients and a nutritionist surrounded by oversized vegetables and fruit"></div>
</section>

<section class="pro">
  <h2 class="abs pro-title">You are a dietitian nutritionist</h2>
  <div class="card" style="left:181px;top:2436px">
    <svg viewBox="0 0 96 96" width="96"><circle cx="48" cy="48" r="40" fill="#22a56c"/></svg>
    <p>Use nutrivana to optimize your activity</p>
  </div>
  <div class="card" style="left:476px;top:2436px">
    <svg viewBox="0 0 96 96" width="96"><circle cx="48" cy="48" r="44" fill="#1fa06a"/><path d="M48 22v28l14 14" fill="none" stroke="#fff" stroke-width="7" stroke-linecap="round" stroke-linejoin="round"/></svg>
    <p>Free up time by making an appointment online</p>
  </div>
  <div class="card" style="left:769px;top:2436px">
    <svg viewBox="0 0 96 96" width="96"><rect x="22" y="14" width="62" height="44" rx="6" fill="#3fbfb2" transform="rotate(-10 53 36)"/><rect x="12" y="32" width="70" height="50" rx="7" fill="#1fa06a"/><rect x="12" y="44" width="70" height="8" fill="#0a8b54"/><rect x="22" y="60" width="16" height="6" rx="2" fill="#fff"/><rect x="22" y="70" width="28" height="4" rx="2" fill="#fff"/></svg>
    <p>Limit unfulfilled appointments with online payment</p>
  </div>
  <div class="card" style="left:181px;top:2760px">
    <svg viewBox="0 0 96 96" width="96"><rect x="18" y="16" width="56" height="70" rx="6" fill="#1fa06a"/><rect x="34" y="10" width="24" height="12" rx="4" fill="#0a8b54"/><rect x="28" y="36" width="8" height="6" fill="#fff"/><rect x="40" y="36" width="24" height="6" fill="#fff"/><rect x="28" y="50" width="8" height="6" fill="#fff"/><rect x="40" y="50" width="24" height="6" fill="#fff"/><rect x="28" y="64" width="8" height="6" fill="#fff"/><rect x="40" y="64" width="24" height="6" fill="#fff"/></svg>
    <p>Take advantage of Nutrivana's notoriety to obtain better visibility</p>
  </div>
  <div class="card" style="left:476px;top:2760px">
    <svg viewBox="0 0 96 96" width="96"><path d="M8 48L48 12l40 36" fill="none" stroke="#1fa06a" stroke-width="9" stroke-linecap="round" stroke-linejoin="round"/><path d="M20 46v38h22V64h12v20h22V46L48 20z" fill="#1fa06a"/></svg>
    <p>Use a commercial platform to develop your patient base</p>
  </div>
  <div class="card" style="left:769px;top:2760px">
    <svg viewBox="0 0 96 96" width="96"><path d="M8 40h40v30H24l-12 10V70H8z" fill="#3fbfb2"/><path d="M24 14h64v40H78v14L64 54H24z" fill="#1fa06a"/><circle cx="44" cy="34" r="3.5" fill="#fff"/><circle cx="56" cy="34" r="3.5" fill="#fff"/><circle cx="68" cy="34" r="3.5" fill="#fff"/></svg>
    <p>Use the platform's communication tools</p>
  </div>
</section>

<footer>
  <ul class="abs footer-links">
    <li>Home</li><li>Professionals</li><li>Search</li><li>Appointment</li><li>Payment</li><li>Blog</li>
  </ul>
  <div class="abs brand footer-brand"><span class="brand-dot"></span>nutrivana</div>
  <ul class="abs contact">
    <li style="top:3401px"><span class="ico"><svg width="22" height="22" viewBox="0 0 24 24"><path d="M6.6 10.8a15 15 0 006.6 6.6l2.2-2.2c.3-.3.7-.4 1-.2 1.1.4 2.3.6 3.6.6.6 0 1 .4 1 1V20c0 .6-.4 1-1 1A17 17 0 013 4c0-.6.4-1 1-1h3.5c.6 0 1 .4 1 1 0 1.3.2 2.5.6 3.6.1.3 0 .7-.2 1z" fill="#fff"/></svg></span><span>Phone<br>+00 4183 5520</span></li>
    <li style="top:3465px"><span class="ico"><svg width="20" height="20" viewBox="0 0 24 24"><rect x="2" y="5" width="20" height="14" rx="2" fill="#fff"/><path d="M3 6l9 7 9-7" fill="none" stroke="#1fa06a" stroke-width="2"/></svg></span><span>Email<br>hello@nutrivana.com</span></li>
    <li style="top:3540px"><span class="ico"><svg width="20" height="22" viewBox="0 0 24 24"><path d="M12 2a7 7 0 00-7 7c0 5 7 13 7 13s7-8 7-13a7 7 0 00-7-7zm0 9.5A2.5 2.5 0 1112 6.5a2.5 2.5 0 010 5z" fill="#fff"/></svg></span><span>Verlanstraat 8, 14<br>3100 Molvenhal</span></li>
  </ul>
  <p class="abs copyright">Copyright © 2022 All Right Reserved</p>
</footer>
</body>
</html>
```